rt for guide - bartholomew finch personal speaking/consulting website

custom website for my personal speaking/consulting services brand, you can see the basic site we are using as a placeholder at www.rtforguide.example now. I want to re-position this to more of a personal brand site and have video samples of speaking events, downloadable content, a video blog, and links to podcast. I really like the design of dorianwelk.example and the feature set should be fairly similar to his. I'll begin to compile more stock images etc. to use for sliders like he has done, for now we'll need to use stock imagery or existing photography from my social accounts. You can get a feel for social at all platforms/bfinchbroker i.e. facebook.com/bfinchbroker. the site should be primarily geared toward showcasing speaking/consulting services and content, as well as be flexible to allow for additional downloadables etc. in the future.

Target Market(s)

entrepreneurs and leaders looking to grow themselves, their business, and those they lead.

Coding

Coded - Design and coding required

Number of Pages Required

3 page

Font styles to use
Sans Serif

Colors

Designer to choose colors to be used in the design.

Requirements
Must have
• modern slick design, video blog, podcast feed, registration for people to subscribe to newsletter

```html
<!DOCTYPE html>
<html lang="en">
<head>
<meta charset="utf-8">
<title>Bartholomew Finch — Speaker &amp; Coach</title>
<link rel="stylesheet" href="https://fonts.googleapis.com/css2?family=Lora:ital,wght@0,400;0,500;1,400&family=Montserrat:wght@400;500&family=Open+Sans:wght@400&display=swap">
<style>
:root{
  --orange:#ff6508;
  --ink:#2a2a2a;
  --muted:#666;
  --light:#f4f4f4;
  --about-bg:#efeff0;
  --dark:#2b2b2b;
  --white:#fff;
}
*{margin:0;padding:0;box-sizing:border-box}
html,body{width:1200px;height:4272px;overflow:hidden}
body{position:relative;background:var(--white);color:var(--ink);font-family:"Open Sans",Arial,sans-serif}
section,header,footer{position:absolute;left:0;width:1200px}
.abs{position:absolute}
.photo{position:absolute}
.serif{font-family:"Lora",Georgia,serif}
.section-title{position:absolute;left:0;width:1200px;text-align:center;font-family:"Lora",Georgia,serif;font-size:40px;font-weight:400;color:var(--ink)}
.section-title::after{content:"";display:block;width:70px;height:3px;background:var(--orange);margin:14px auto 0}

/* hero */
.hero{top:0;height:728px;background:linear-gradient(100deg,#8a8580 0%,#6f6a66 35%,#3e4a70 70%,#1f2d5e 100%)}
.hero .photo{inset:0}
.site-nav{position:absolute;top:48px;left:0;width:1200px;height:40px}
.brand{position:absolute;left:112px;top:0;font-family:"Lora",Georgia,serif;font-size:34px;color:var(--white)}
.menu{position:absolute;left:475px;top:12px;display:flex;gap:0;list-style:none}
.menu li{font-family:"Montserrat",Arial,sans-serif;font-size:12px;color:var(--white);letter-spacing:.3px;margin-right:45px}
.hero-card{position:absolute;left:98px;top:283px;width:532px;height:274px;background:rgba(90,90,90,.72);padding:30px 33px}
.hero-card h1{font-family:"Lora",Georgia,serif;font-weight:400;font-size:60px;color:var(--orange);line-height:1.1}
.hero-card p{margin-top:14px;font-family:"Lora",Georgia,serif;font-style:italic;font-size:20px;line-height:38px;color:var(--white)}

/* about */
.about{top:728px;height:569px;background:var(--about-bg)}
.about .photo{left:91px;top:10px;width:572px;height:559px;background:radial-gradient(ellipse at 50% 45%,#d9b49a 0%,#8c6b58 35%,#2e3448 70%,var(--about-bg) 100%)}
.about h2{position:absolute;left:712px;top:60px;font-family:"Lora",Georgia,serif;font-weight:400;font-size:68px;color:var(--ink)}
.about p{position:absolute;left:711px;width:374px;font-family:"Lora",Georgia,serif;font-style:italic;font-size:13px;line-height:27.5px;color:#333;text-align:justify}
.btn-pill{position:absolute;left:711px;top:467px;width:161px;height:53px;border-radius:27px;background:var(--orange);color:var(--white);font-family:"Lora",Georgia,serif;font-size:16px;line-height:53px;text-align:center}

/* events */
.events{top:1297px;height:582px;background:var(--light)}
.card{position:absolute;top:123px;width:310px}
.card .photo{position:relative;width:310px;height:239px}
.date{position:absolute;left:0;top:83px;width:50px;height:88px;background:var(--orange)}
.date .day{position:absolute;left:0;top:44px;width:50px;height:44px;background:#2a2a2a;color:var(--white);text-align:center;font-family:"Montserrat",Arial,sans-serif;font-size:20px;line-height:24px;padding-top:4px}
.date .day small{display:block;font-size:9px;line-height:10px}
.date svg{position:absolute;left:17px;top:14px}
.card h3{margin-top:25px;font-family:"Lora",Georgia,serif;font-weight:400;font-size:21px;color:var(--ink)}
.card p{margin-top:14px;font-size:11.5px;line-height:26px;color:var(--muted)}
.card a{display:block;margin-top:10px;font-family:"Lora",Georgia,serif;font-size:14px;color:var(--orange)}

/* services */
.services{top:1879px;height:433px;background:var(--orange)}
.services .section-title{color:var(--white)}
.services .section-title::after{background:var(--white)}
.service{position:absolute;top:148px;width:220px;text-align:center;color:var(--white)}
.service .ring{width:118px;height:118px;border-radius:50%;background:var(--white);margin:0 auto;display:flex;align-items:center;justify-content:center}
.service h3{margin-top:24px;font-family:"Lora",Georgia,serif;font-weight:400;font-size:20px}
.service p{margin-top:12px;font-size:11.5px;line-height:24px}

/* video */
.video{top:2312px;height:520px;background:var(--white)}
.play{position:absolute;width:83px;height:83px;border:3px solid var(--white);border-radius:50%;background:rgba(0,0,0,.25)}
.play::after{content:"";position:absolute;left:32px;top:24px;border-left:24px solid var(--white);border-top:15px solid transparent;border-bottom:15px solid transparent}
.feature-video{top:2832px;height:416px;background:linear-gradient(90deg,#3b3633,#5a4f47 45%,#3a3230)}

/* podcast */
.podcast{top:3248px;height:641px;background:var(--white)}
.pod{position:absolute;top:129px;width:310px;text-align:center}
.pod .photo{position:relative;width:310px;height:237px}
.pod .photo svg{position:absolute;left:125px;top:88px}
.pod h3{margin-top:32px;font-family:"Lora",Georgia,serif;font-weight:400;font-size:20px}
.pod p{margin-top:14px;font-size:11.5px;line-height:26px;color:var(--muted)}
.btn-outline{display:inline-block;margin-top:22px;width:114px;height:40px;border:1px solid var(--orange);color:var(--orange);font-family:"Lora",Georgia,serif;font-size:12px;line-height:38px}

/* newsletter */
.newsletter{top:3889px;height:124px;background:var(--orange)}
.newsletter h2{position:absolute;left:146px;top:38px;font-family:"Lora",Georgia,serif;font-weight:400;font-size:38px;color:var(--white)}
.newsletter .field{position:absolute;left:482px;top:38px;width:459px;height:48px;background:var(--white);font-size:11px;line-height:48px;padding-left:20px;color:#333}
.newsletter .submit{position:absolute;left:941px;top:38px;width:116px;height:48px;background:var(--dark);color:var(--white);font-family:"Lora",Georgia,serif;font-size:18px;line-height:48px;text-align:center}

/* footer */
.site-footer{top:4013px;height:259px;background:var(--dark);color:var(--white);text-align:center}
.site-footer .brand{position:static;display:block;margin-top:40px;font-size:36px}
.foot-menu{display:flex;justify-content:center;margin-top:22px;list-style:none;font-family:"Montserrat",Arial,sans-serif;font-size:12px}
.foot-menu li+li::before{content:"|";margin:0 20px}
.social{display:flex;justify-content:center;gap:6px;margin-top:24px}
.social span{width:28px;height:28px;border:1.5px solid var(--white);border-radius:50%}
.copy{margin-top:18px;font-size:12px}
</style>
</head>
<body>

<header class="hero">
  <div class="photo" role="img" aria-label="Video still of the speaker talking in front of a whiteboard"></div>
  <nav class="site-nav">
    <div class="brand">Bartholomew Finch</div>
    <ul class="menu">
      <li>HOME</li><li>ABOUT</li><li>PODCAST</li><li>VIDEO</li><li>BLOG</li><li>EVENTS</li><li>CONTACT US</li>
    </ul>
  </nav>
  <div class="hero-card">
    <h1>Bartholomew Finch</h1>
    <p>Sed ut perspiciatis unde omnis iste natus error sit voluptatem accusantium doloremque laudantium, totam rem aperiam</p>
  </div>
</header>

<section class="about">
  <div class="photo" role="img" aria-label="Portrait of the speaker smiling"></div>
  <h2>About Me</h2>
  <p style="top:168px">Sed ut perspiciatis unde omnis iste natus error sit voluptatem accusantium doloremque laudantium, totam rem aperiam, eaq ue ipsa quae ab illo inventore veritatis et quasi architecto bea tae vitae dicta sunt explicabo. Nemo enim ipsam volup tatem quia voluptas sit aspernatur aut odit aut fugit, sed quia ratione voluptatem sequi nesciunt.</p>
  <p style="top:360px">Neque porro quisquam est, qui dolorem ipsum quia dolor sit amet, consectetur, adipisci velit, sed quia non numquam eius ut dolore magnam aliquam quaerat voluptatem.</p>
  <div class="btn-pill">Download Now</div>
</section>

<section class="events">
  <h2 class="section-title" style="top:30px">Speaking Events</h2>
  <article class="card" style="left:111px">
    <div class="photo" style="background:linear-gradient(160deg,#9fb6c9,#c9d1d6 45%,#6d8a4c)" role="img" aria-label="Event photo of a balloon figure at a waterfront venue">
      <div class="date"><svg width="16" height="16" viewBox="0 0 16 16" fill="none" stroke="#fff" stroke-width="1.5"><rect x="1" y="3" width="14" height="12"/><path d="M1 7h14M5 1v4M11 1v4"/></svg><div class="day">02<small>OCT</small></div></div>
    </div>
    <h3>Sed ut perspiciatis unde omnis</h3>
    <p>Sed ut perspiciatis unde omnis iste natus error sit volupta tem accusantium doloremque laudantium, totam rem ipsa quae ab illo inventore veritatis</p>
    <a>Read More</a>
  </article>
  <article class="card" style="left:446px">
    <div class="photo" style="background:linear-gradient(160deg,#7d8fa3,#3f5270 50%,#8b8f94)" role="img" aria-label="Event photo of a pickup truck on display">
      <div class="date"><svg width="16" height="16" viewBox="0 0 16 16" fill="none" stroke="#fff" stroke-width="1.5"><rect x="1" y="3" width="14" height="12"/><path d="M1 7h14M5 1v4M11 1v4"/></svg><div class="day">02<small>OCT</small></div></div>
    </div>
    <h3>Sed ut perspiciatis unde omnis</h3>
    <p>Sed ut perspiciatis unde omnis iste natus error sit volupta tem accusantium doloremque laudantium, totam rem ipsa quae ab illo inventore veritatis</p>
    <a>Read More</a>
  </article>
  <article class="card" style="left:779px">
    <div class="photo" style="background:linear-gradient(120deg,#b89a7d,#d8b89c 50%,#5a4e48)" role="img" aria-label="Selfie of the speaker with a guest at an event">
      <div class="date"><svg width="16" height="16" viewBox="0 0 16 16" fill="none" stroke="#fff" stroke-width="1.5"><rect x="1" y="3" width="14" height="12"/><path d="M1 7h14M5 1v4M11 1v4"/></svg><div class="day">02<small>OCT</small></div></div>
    </div>
    <h3>Sed ut perspiciatis unde omnis</h3>
    <p>Sed ut perspiciatis unde omnis iste natus error sit volupta tem accusantium doloremque laudantium, totam rem ipsa quae ab illo inventore veritatis</p>
    <a>Read More</a>
  </article>
</section>

<section class="services">
  <h2 class="section-title" style="top:36px">Our Services</h2>
  <div class="service" style="left:125px">
    <div class="ring"><svg width="60" height="60" viewBox="0 0 60 60" fill="none" stroke="#ff6508" stroke-width="2"><circle cx="16" cy="10" r="5"/><circle cx="30" cy="10" r="5"/><circle cx="44" cy="10" r="5"/><path d="M9 40V22h14v18M23 40V22h14v18M37 40V22h14v18M6 50h48M12 50V44M20 50V44M28 50V44M36 50V44M44 50V44"/></svg></div>
    <h3>Leadership Skills</h3>
    <p>Sed ut perspiciatis unde omnis iste<br>natus error sit voluptatem</p>
  </div>
  <div class="service" style="left:371px">
    <div class="ring"><svg width="60" height="60" viewBox="0 0 60 60" fill="none" stroke="#ff6508" stroke-width="2"><circle cx="30" cy="12" r="5"/><path d="M23 28c0-6 14-6 14 0M30 28v8M14 40l16-4 16 4"/><circle cx="14" cy="40" r="4"/><circle cx="46" cy="40" r="4"/><circle cx="30" cy="42" r="4"/><path d="M6 54c0-6 16-6 16 0M22 54c0-6 16-6 16 0M38 54c0-6 16-6 16 0"/></svg></div>
    <h3>Team Building</h3>
    <p>Sed ut perspiciatis unde omnis iste<br>natus error sit voluptatem</p>
  </div>
  <div class="service" style="left:616px">
    <div class="ring"><svg width="60" height="60" viewBox="0 0 60 60" fill="none" stroke="#ff6508" stroke-width="2.5"><rect x="8" y="18" width="44" height="30" rx="3"/><path d="M22 18v-6h16v6M8 30h44M26 30v4h8v-4"/></svg></div>
    <h3>Entrepreneurs</h3>
    <p>Sed ut perspiciatis unde omnis iste<br>natus error sit voluptatem</p>
  </div>
  <div class="service" style="left:863px">
    <div class="ring"><svg width="60" height="60" viewBox="0 0 60 60" fill="none" stroke="#ff6508" stroke-width="2"><rect x="6" y="10" width="48" height="40" rx="3"/><path d="M6 18h48"/><circle cx="20" cy="32" r="5"/><path d="M11 44c0-6 18-6 18 0"/><circle cx="40" cy="34" r="8"/><path d="M36 34l3 3 5-6"/></svg></div>
    <h3>Personal Coaching</h3>
    <p>Sed ut perspiciatis unde omnis iste<br>natus error sit voluptatem</p>
  </div>
</section>

<section class="video">
  <h2 class="section-title" style="top:28px">Video Blog</h2>
  <div class="photo" style="left:111px;top:134px;width:474px;height:330px;background:linear-gradient(180deg,#3b4454,#2a3444 45%,#23304e)" role="img" aria-label="Video still of a crowded stadium">
    <span class="play" style="left:195px;top:123px"></span>
  </div>
  <div class="photo" style="left:615px;top:134px;width:474px;height:330px;background:linear-gradient(120deg,#6b5340,#c9b49a 45%,#7a6a5c)" role="img" aria-label="Video still of a small dog waiting for a treat">
    <span class="play" style="left:195px;top:123px"></span>
  </div>
</section>

<section class="feature-video" role="img" aria-label="Featured video still of the speaker with a guest">
  <span class="play" style="left:558px;top:167px"></span>
</section>

<section class="podcast">
  <h2 class="section-title" style="top:30px">Podcast Feed</h2>
  <article class="pod" style="left:111px">
    <div class="photo" style="background:linear-gradient(120deg,#5a5a6a,#8e8c95 50%,#4c5a7a)" role="img" aria-label="Photo of the speaker with a guest at a conference">
      <svg width="60" height="60" viewBox="0 0 60 60" fill="none" stroke="#fff" stroke-width="4"><path d="M14 40a20 20 0 1 1 32 0"/><path d="M21 34a11 11 0 1 1 18 0"/><circle cx="30" cy="28" r="5" fill="#fff"/><path d="M30 34v20"/></svg>
    </div>
    <h3>Sed ut perspiciatis unde</h3>
    <p>Sed ut perspiciatis unde omnis iste natus error sit volupta tem accusantium doloremque laudantium, ipsa quae ab illo inventore veritatis</p>
    <span class="btn-outline">READ MORE</span>
  </article>
  <article class="pod" style="left:446px">
    <div class="photo" style="background:linear-gradient(150deg,#c9a27a,#e8d8c4 45%,#8a6a56)" role="img" aria-label="Photo of an event tent interior">
      <svg width="60" height="60" viewBox="0 0 60 60" fill="none" stroke="#fff" stroke-width="4"><path d="M14 40a20 20 0 1 1 32 0"/><path d="M21 34a11 11 0 1 1 18 0"/><circle cx="30" cy="28" r="5" fill="#fff"/><path d="M30 34v20"/></svg>
    </div>
    <h3>Sed ut perspiciatis unde</h3>
    <p>Sed ut perspiciatis unde omnis iste natus error sit volupta tem accusantium doloremque laudantium, ipsa quae ab illo inventore veritatis</p>
    <span class="btn-outline">READ MORE</span>
  </article>
  <article class="pod" style="left:779px">
    <div class="photo" style="background:linear-gradient(120deg,#4a4846,#8a7c70 50%,#3c3a3a)" role="img" aria-label="Photo of the speaker with a guest seated in an audience">
      <svg width="60" height="60" viewBox="0 0 60 60" fill="none" stroke="#fff" stroke-width="4"><path d="M14 40a20 20 0 1 1 32 0"/><path d="M21 34a11 11 0 1 1 18 0"/><circle cx="30" cy="28" r="5" fill="#fff"/><path d="M30 34v20"/></svg>
    </div>
    <h3>Sed ut perspiciatis unde</h3>
    <p>Sed ut perspiciatis unde omnis iste natus error sit volupta tem accusantium doloremque laudantium, ipsa quae ab illo inventore veritatis</p>
    <span class="btn-outline">READ MORE</span>
  </article>
</section>

<section class="newsletter">
  <h2>Newsletter Signup :</h2>
  <div class="field">Enter Your Email id :</div>
  <div class="submit">Signup</div>
</section>

<footer class="site-footer">
  <div class="brand">Bartholomew Finch</div>
  <ul class="foot-menu">
    <li>HOME</li><li>ABOUT</li><li>PODCAST</li><li>VIDEO</li><li>BLOG</li><li>EVENTS</li><li>CONTACT US</li>
  </ul>
  <div class="social"><span></span><span></span><span></span></div>
  <p class="copy">© Copyright 2019 Bartholomew Finch.All Rights Reserved.</p>
</footer>

</body>
</html>
```